mykelvoratrim needs a package design

myKelvoraTrim - a individual micronutrient product for sporty people. We want to sell individual micronutrients to / for high performance sportsmen. (Granules.jpg eg.) The recipes are based on our customer's answers in a questionnaire. As the name of our product myKelvoraTrim tells, our target audience are healthy sportsmen aged in between 30 to 60 years with a higher level of income. We already have a logo, now we need a design for our cans. The size of the can-area is 245x180mm a 3mm border. Consider the attachement. The logo has to be on the design. Additionally a 70x45mm clean space needs to be on it, we will stick a transparent label with personalData of our customers on it. (Eg. "Hobbs mixture") The fontcolour will be black for the customers dataonly. The label printer doze support colors. You may add a name and a slight border in the design, so we can imagine how it looks better on the can. The font used for the logo is "Good Times".

Industry/Entity Type

Product

Font styles to use
Serif
Sans Serif

Requirements
Should not have
• We do not need any information about content on the can (magnesium ...), this will be on the package insert.

```html
<!DOCTYPE html>
<html lang="en">
<head>
<meta charset="utf-8">
<title>myKelvoraTrim – Granules Can Wrap</title>
<link rel="stylesheet" href="https://fonts.googleapis.com/css2?family=Josefin+Sans:wght@300;400;600;700&display=swap">
<style>
  :root {
    --silver-edge: #b9bebd;
    --silver-mid: #d6dad9;
    --silver-light: #eef0ef;
    --ink: #1c1c1c;
    --ink-soft: #333536;
    --label-ink: #000000;
    --brand-blue: #1f7fc4;
    --rule: #4a4c4d;
    --label-border: #8d9291;
  }
  * { margin: 0; padding: 0; box-sizing: border-box; }
  html, body {
    width: 788px;
    height: 1200px;
    overflow: hidden;
  }
  body {
    font-family: "Josefin Sans", sans-serif;
    color: var(--ink);
    background: linear-gradient(90deg,
      var(--silver-edge) 0%,
      var(--silver-mid) 22%,
      var(--silver-light) 52%,
      var(--silver-mid) 78%,
      var(--silver-edge) 100%);
  }
  .wrap {
    position: relative;
    width: 788px;
    height: 1200px;
    text-align: center;
  }
  .brand {
    position: absolute;
    top: 284px;
    left: 0;
    right: 0;
    display: flex;
    justify-content: center;
    align-items: center;
    gap: 10px;
  }
  .brand-dot {
    width: 12px;
    height: 12px;
    border-radius: 50%;
    background: var(--brand-blue);
  }
  .brand-name {
    font-weight: 600;
    font-size: 34px;
    line-height: 40px;
    color: var(--brand-blue);
  }
  .product-name {
    position: absolute;
    top: 480px;
    left: 0; right: 0;
    font-weight: 400;
    font-size: 32px;
    line-height: 36px;
    letter-spacing: 13px;
    padding-left: 13px;
  }
  .tagline {
    position: absolute;
    top: 542px;
    left: 0; right: 0;
    font-weight: 300;
    font-size: 16px;
    line-height: 22px;
    letter-spacing: 1px;
    color: var(--ink-soft);
  }
  .label-space {
    position: absolute;
    top: 628px;
    left: 254px;
    width: 280px;
    height: 180px;
    border: 1px solid var(--label-border);
    display: flex;
    align-items: center;
    justify-content: center;
  }
  .label-name {
    font-weight: 400;
    font-size: 22px;
    color: var(--label-ink);
  }
  .claims {
    position: absolute;
    top: 836px;
    left: 0; right: 0;
    list-style: none;
    display: flex;
    flex-direction: column;
    align-items: center;
  }
  .claim {
    font-weight: 300;
    font-size: 16px;
    letter-spacing: 1.2px;
    color: var(--ink-soft);
    height: 31px;
    line-height: 26px;
  }
  .claim-rule {
    width: 184px;
    height: 1px;
    background: var(--rule);
    margin-top: -4px;
    margin-bottom: 4px;
  }
  .quality {
    position: absolute;
    top: 966px;
    left: 0; right: 0;
  }
  .quality-mark {
    font-weight: 700;
    font-size: 18px;
    letter-spacing: 3px;
    padding-left: 3px;
  }
  .quality-note {
    font-weight: 400;
    font-size: 18px;
    letter-spacing: 1.2px;
    color: var(--ink-soft);
    margin-top: 4px;
  }
</style>
</head>
<body>
  <main class="wrap">
    <header class="brand">
      <span class="brand-dot"></span>
      <span class="brand-name">myKelvoraTrim</span>
    </header>

    <h1 class="product-name">GRANULES</h1>

    <p class="tagline">micronutrients food<br>supplements tailored for high<br>performance sportsman</p>

    <section class="label-space" aria-label="Clean space for personal label, 70 x 45 mm">
      <span class="label-name">Hobbs mixture</span>
    </section>

    <ul class="claims">
      <li class="claim">increases energy</li>
      <li class="claim-rule"></li>
      <li class="claim">relieves muscle aches</li>
      <li class="claim-rule"></li>
      <li class="claim">improves heart health</li>
    </ul>

    <footer class="quality">
      <div class="quality-mark">GMP</div>
      <div class="quality-note">Certified</div>
    </footer>
  </main>
</body>
</html>
```